Powerpoint contest

We need to re-design our powerpoints to be much more consistent. All the details are mentioned here. I have more than 30 slides to be created in all.

https://www.pagewell.io/brivane/All-Powerpoints-3c81d27e90ab4f51a6c2e04b7d9f1a25

Requirements
Must have
• Colors should be greyscale and kvelcom pink (ea0a8e) used in small amounts just for accents.

```html
<!DOCTYPE html>
<html lang="en">
<head>
<meta charset="utf-8">
<title>Brivane Presentation Template</title>
<link href="https://fonts.googleapis.com/css2?family=Ubuntu:wght@300;400;500;700&display=swap" rel="stylesheet">
<style>
:root{
  --pink:#ea0a8e;
  --ink:#2b2b2b;
  --grey:#6d6d6d;
  --soft:#9a9a9a;
  --mist:#dce5ea;
  --mist-2:#c9d5dc;
  --page:#a9b2bd;
  --plum:#8e8189;
  --teal:#3d8b80;
}
*{box-sizing:border-box;margin:0;padding:0}
html,body{width:1200px;height:1200px;overflow:hidden}
body{background:var(--page);font-family:'Ubuntu',sans-serif;color:var(--ink);position:relative}
.slide{position:absolute;width:293px;height:176px;background:#fff;overflow:hidden;box-shadow:0 1px 4px rgba(0,0,0,.12)}
.abs{position:absolute}
.photo{position:absolute}
.logo{position:absolute;font-weight:700;color:var(--ink);display:flex;align-items:center;gap:2px;line-height:1}
.logo::before{content:"";width:.62em;height:.62em;border-radius:50%;background:var(--pink);display:block}
.heading{position:absolute;left:15px;top:13px;font-weight:700;font-size:9.5px;letter-spacing:.2px}
.heading::after{content:"";position:absolute;left:0;bottom:-3px;width:12px;height:1.4px;background:var(--pink)}
.foot{position:absolute;left:11px;bottom:8px;font-size:3.4px;color:var(--soft)}
.pager{position:absolute;right:5px;bottom:6px;display:flex;align-items:center;gap:1.5px}
.pager i{width:1.8px;height:1.8px;border-radius:50%;background:var(--pink);display:block}
.pager i+i{background:#e88}
.pager b{width:19px;height:6px;border-radius:3px;background:#cfd6db;font-size:3.5px;color:#fff;font-weight:400;text-align:center;line-height:6px}
.tiny{font-size:3.6px;line-height:1.35;color:var(--grey)}
.micro{font-size:3px;line-height:1.35;color:var(--grey)}
.title-lg{font-size:13.5px;font-weight:400;line-height:1.28;color:var(--ink)}
.sub{font-size:6.5px;color:var(--ink)}
.band{position:absolute;left:0;right:0;bottom:0;height:46px;background:var(--mist)}
.meta{position:absolute;font-size:4.2px;color:var(--grey);line-height:1.5}
.meta b{color:var(--ink)}
.label{font-size:4.2px;font-weight:700;color:var(--ink)}
.stat-ico{position:absolute;left:14px;width:14px;height:14px}
.bar-row{display:flex;align-items:center;gap:3px;height:5px}
.bar-row span{width:38px;font-size:2.8px;color:var(--grey)}
.bar-row em{display:block;height:3.2px;background:#8f8f8f;font-style:normal;font-size:2.6px;color:#fff;padding-left:1px;line-height:3.2px}
.cust-grid{position:absolute;display:grid}
.cust-grid div{height:11px;background:#fff}
.cust-head{position:absolute;left:117px;top:27px;display:grid;grid-template-columns:repeat(6,22px);font-size:3px;font-weight:700;color:var(--ink)}
.card-photo{position:absolute;width:57px;height:52px}
.card-info{position:absolute;width:64px;height:52px;padding:4px 6px;border:.6px solid #d9dfe3}
.card-info h4{font-size:5.6px;font-weight:400;line-height:1.1}
.card-info h5{font-size:2.8px;font-weight:400;margin-bottom:3px}
.card-info p{font-size:2.8px;line-height:1.35}
.num-list{position:absolute;display:grid;row-gap:5px}
.num{display:flex;gap:4px;font-size:4.5px;font-weight:700}
.num p{font-weight:300;font-size:2.9px;line-height:1.3;color:var(--grey);font-style:italic;width:48px}
.svc{position:absolute;width:85px;height:56px;background:var(--mist);padding:4px 5px}
.svc h6{font-size:3.6px;font-weight:500;margin-bottom:4px;display:flex;align-items:center;gap:2px}
.svc h6::before{content:"";width:2.2px;height:2.2px;border-left:.6px solid var(--ink);border-top:.6px solid var(--ink)}
.svc p{font-size:3.1px;line-height:1.4;color:var(--grey);letter-spacing:.3px}
.col3{position:absolute;width:85px;top:36px}
.col3 .ph{height:62px;background:var(--mist);display:flex;flex-direction:column;align-items:center;padding-top:8px;font-size:2.8px;color:#fff;text-align:center;line-height:1.3}
.col3 .ph svg{margin-top:9px}
.col3 h6{font-size:5px;font-weight:400;text-align:center;margin:4px 0 3px}
.col3 p{font-size:2.9px;text-align:center;color:var(--grey);line-height:1.35}
.office{position:absolute;font-size:3.4px;line-height:1.3;color:var(--ink)}
.office b{display:block;font-size:3.6px}
.disclaimer-body{position:absolute;left:98px;top:39px;width:176px;font-size:4.5px;line-height:6.7px;color:var(--grey);text-align:left}
</style>
</head>
<body>

<!-- Row 1 -->
<section class="slide" style="left:127px;top:8px">
  <div class="photo" role="img" aria-label="Faded grey city tower backdrop" style="left:0;top:0;width:293px;height:130px;background:linear-gradient(110deg,#f6f7f8 0%,#e6e8ea 35%,#f4f5f6 70%,#fff 100%)"></div>
  <div class="abs" style="left:0;top:0;width:2.5px;height:130px;background:var(--pink)"></div>
  <div class="logo" style="right:20px;top:22px;font-size:15px">Brivane</div>
  <div class="abs" style="left:19px;top:66px"><div class="title-lg">Place the Document’s<br>Presentation Title Here</div><div class="sub" style="margin-top:2px">Subtitle Highlights Here</div></div>
  <div class="band"></div>
  <div class="meta" style="left:19px;top:148px">March 19, 2020<br>PROPOSAL FOR: <b>COMPANY-X</b></div>
  <div class="meta" style="right:16px;top:157px">www.brivane.com</div>
</section>

<section class="slide" style="left:450px;top:8px">
  <div class="photo" role="img" aria-label="Business team collaborating in a bright office" style="left:0;top:0;width:293px;height:130px;background:linear-gradient(90deg,#fafafa 0%,#eceeef 35%,#c9ccd0 65%,#8f97a3 100%)"></div>
  <div class="abs" style="left:18px;top:66px"><div class="title-lg">Place the Document’s<br>Presentation Title Here</div><div class="sub" style="margin-top:2px">Subtitle Highlights Here</div></div>
  <div class="band"></div>
  <div class="meta" style="left:19px;top:148px">March 19, 2020<br>PROPOSAL FOR: <b>COMPANY-X</b></div>
  <div class="logo" style="right:17px;top:144px;font-size:10px">Brivane</div>
  <div class="meta" style="right:17px;top:157px">www.brivane.com</div>
</section>

<section class="slide" style="left:774px;top:8px">
  <div class="photo" role="img" aria-label="Silhouetted colleagues by a window at sunset" style="left:0;top:0;width:293px;height:143px;background:linear-gradient(160deg,#2c2a55 0%,#6a6f9a 40%,#a7b3c9 65%,#5a4f79 100%)"></div>
  <div class="abs" style="left:17px;top:87px;width:262px;height:52px;background:rgba(235,238,243,.78)"></div>
  <div class="abs" style="left:27px;top:93px"><div class="title-lg">Place the Document’s<br>Presentation Title Here</div></div>
  <div class="meta" style="left:22px;top:151px">March 19, 2020<br>PROPOSAL FOR: <b>COMPANY-X</b></div>
  <div class="logo" style="right:10px;top:154px;font-size:11px">Brivane</div>
</section>

<!-- Row 2 -->
<section class="slide" style="left:127px;top:204px">
  <div class="logo" style="right:19px;top:19px;font-size:9px">Brivane</div>
  <div class="abs" style="left:16px;top:40px;font-size:11px">DISCLAIMER</div>
  <div class="abs" style="left:16px;top:54px;font-size:6px;color:var(--grey)">Put some text here</div>
  <div class="abs" style="left:18px;top:64px;width:13px;height:1.3px;background:var(--pink)"></div>
  <p class="disclaimer-body">Maecenas sed diam eget risus varius blandit sit amet non magna. Donec id elit non mi porta gravida at eget metus. Maecenas sed diam eget risus varius blandit sit amet non magna. Donec id elit non mi porta gravida at eget metus. Maecenas sed diam eget risus varius blandit sit amet non magna. Donec id elit non mi porta gravida at eget metus. Maecenas sed diam eget risus varius blandit sit amet non magna. Donec id elit non mi porta gravida at eget metus. Maecenas sed diam eget risus varius blandit sit amet non magna. Donec id elit non mi porta gravida at eget metus. Maecenas sed diam eget risus varius blandit sit amet non magna. Donec id elit non mi porta gravida at eget metus. Maecenas sed diam eget risus varius blandit sit amet non magna.</p>
  <div class="foot">Presentation Title goes here | www.brivane.com</div>
  <div class="pager"><i></i><i></i><b>01</b></div>
</section>

<section class="slide" style="left:450px;top:204px">
  <div class="photo" role="img" aria-label="Black and white office window overlooking city towers with people" style="left:0;top:0;width:293px;height:128px;background:linear-gradient(180deg,#5a5a5a 0%,#c4c4c4 45%,#8c8c8c 75%,#3a3a3a 100%)"></div>
  <div class="abs" style="left:71px;top:139px;font-size:8.5px;display:flex;align-items:center;gap:3px">WHY <span class="logo" style="position:static;font-size:8.5px">Brivane</span></div>
  <div class="abs tiny" style="left:158px;top:139px;font-size:3.8px;color:var(--ink)">All Gain, No Pain.<br>We’re proudly different from other solutions.<br>See what that means for you.</div>
</section>

<section class="slide" style="left:774px;top:204px">
  <div class="photo" role="img" aria-label="Black and white office window overlooking city towers with people" style="left:0;top:0;width:293px;height:176px;background:linear-gradient(180deg,#505050 0%,#c8c8c8 40%,#9a9a9a 70%,#3c3c3c 100%)"></div>
  <div class="abs" style="left:56px;top:140px;width:237px;height:15px;background:var(--pink);color:#fff;font-size:8.5px;line-height:15px;padding-left:5px">01 | SLIDE DIVIDER</div>
</section>

<!-- Row 3 -->
<section class="slide" style="left:127px;top:403px">
  <div class="abs" style="left:0;top:0;width:127px;height:176px;background:#fbfbfc"></div>
  <svg class="stat-ico" style="top:18px" viewBox="0 0 14 14" fill="none" stroke="#ea0a8e" stroke-width="1"><path d="M4 2h6v4a3 3 0 0 1-6 0z M7 9v3 M4.5 12.5h5"/></svg>
  <div class="abs" style="left:44px;top:17px;width:78px"><div class="label">Winner of the<br>Stratusline Partner<br>Innovation Award</div><div class="micro" style="margin-top:1px">Five-star rating on the Stratusline exchange, with over 200 verified client reviews.</div></div>
  <svg class="stat-ico" style="top:52px" viewBox="0 0 14 14" fill="none" stroke="#ea0a8e" stroke-width="1"><circle cx="5" cy="9" r="3"/><path d="M8 12V4 M8 6c2-3 4-2 4-2"/></svg>
  <div class="abs" style="left:44px;top:52px;width:78px"><div class="label">Financial Strength</div><div class="micro">Brivane has shown steady growth and positive cash flow since launch, with most earnings reinvested back into the company.</div></div>
  <svg class="stat-ico" style="top:87px" viewBox="0 0 14 14" fill="none" stroke="#ea0a8e" stroke-width="1"><path d="M1 12l4-4 3 3 5-6 M10 5h3v3"/></svg>
  <div class="abs" style="left:44px;top:86px"><div class="label">Revenue Investments</div>
    <div class="bar-row" style="margin-top:2px"><span>Sales and Marketing</span><em style="width:24px">32%</em></div>
    <div class="bar-row"><span>Research Development</span><em style="width:18px">28%</em></div>
    <div class="bar-row"><span>Customer Satisfaction</span><em style="width:14px">18%</em></div>
    <div class="bar-row"><span>Retain Earnings</span><em style="width:12px">14%</em></div></div>
  <svg class="stat-ico" style="top:137px" viewBox="0 0 14 14" fill="none" stroke="#ea0a8e" stroke-width="1"><path d="M2 11h10l1-7-3 3-3-5-3 5-3-3z"/></svg>
  <div class="abs" style="left:44px;top:136px"><div class="label">Customer Satisfaction</div><div class="micro"><b style="color:#333;font-size:4px">103%</b> Revenue Retention<br><b style="color:#333;font-size:4px">98.2%</b> Customer would recommend</div></div>
  <div class="heading" style="left:143px;top:16px;font-size:8.5px">ABOUT BRIVANE</div>
  <p class="abs micro" style="left:143px;top:31px;width:140px">Brivane is an international software company that has pioneered the cloud application life cycle development sector. Our firm is focused on transforming the release experience for our clients, allowing them to accelerate their operational agility and improve collaboration. The unique architecture of our products provides security, governance and compliance abilities that are unparalleled in the industry. We are trusted by some of the largest brands around the world and provide customized assistance, training and knowledge transfer to each of our customers who operate in a multitude of industries.</p>
  <div class="abs" style="left:143px;top:88px;font-size:3.6px;font-weight:700;color:var(--pink)">BRIVANE SOLUTION</div>
  <div class="abs micro" style="left:143px;top:94px;width:70px"><b style="color:#333">☐ Release Management</b><br>Native cloud application lifecycle management solution that enables code repository, environment management, conflict management and release sync.</div>
  <div class="abs micro" style="left:215px;top:94px;width:68px"><b style="color:#333">☐ Data Migration</b><br>Native data migration tool that allows developers to easily move an entire hierarchy of data while maintaining all relationships.</div>
  <div class="abs" style="left:143px;top:128px;font-size:3.6px;font-weight:700;color:var(--pink)">COMPANY METRICS</div>
  <ul class="abs micro" style="left:148px;top:134px;width:135px">
    <li>Founded in 2014 by an ex-cloud platform employee</li>
    <li>Headquartered in Larkfield, CA</li>
    <li>Two development centers in Eastern Europe and India</li>
    <li>Three support centers in the US, Eastern Europe and India</li>
  </ul>
  <div class="foot">Presentation Title goes here | www.brivane.com</div>
  <div class="pager"><i></i><i></i><b>02</b></div>
</section>

<section class="slide" style="left:450px;top:403px">
  <div class="abs" style="left:0;top:0;width:132px;height:176px;background:#fbfbfc"></div>
  <svg class="stat-ico" style="top:18px" viewBox="0 0 14 14" fill="none" stroke="#ea0a8e" stroke-width="1"><path d="M4 2h6v4a3 3 0 0 1-6 0z M7 9v3 M4.5 12.5h5"/></svg>
  <div class="abs" style="left:44px;top:17px;width:80px"><div class="label">Winner of the<br>Stratusline Partner<br>Innovation Award</div><div class="micro" style="margin-top:1px">Five-star rating on the Stratusline exchange, with over 200 verified client reviews.</div></div>
  <svg class="stat-ico" style="top:52px" viewBox="0 0 14 14" fill="none" stroke="#ea0a8e" stroke-width="1"><circle cx="5" cy="9" r="3"/><path d="M8 12V4 M8 6c2-3 4-2 4-2"/></svg>
  <div class="abs" style="left:44px;top:52px;width:80px"><div class="label">Financial Strength</div><div class="micro">Brivane has shown steady growth and positive cash flow since launch, with most earnings reinvested back into the company.</div></div>
  <svg class="stat-ico" style="top:87px" viewBox="0 0 14 14" fill="none" stroke="#ea0a8e" stroke-width="1"><path d="M1 12l4-4 3 3 5-6 M10 5h3v3"/></svg>
  <div class="abs" style="left:44px;top:86px"><div class="label">Revenue Investments</div>
    <div class="bar-row" style="margin-top:2px"><span>Sales and Marketing</span><em style="width:24px">32%</em></div>
    <div class="bar-row"><span>Research Development</span><em style="width:18px">28%</em></div>
    <div class="bar-row"><span>Customer Satisfaction</span><em style="width:14px">18%</em></div>
    <div class="bar-row"><span>Retain Earnings</span><em style="width:12px">14%</em></div></div>
  <svg class="stat-ico" style="top:137px" viewBox="0 0 14 14" fill="none" stroke="#ea0a8e" stroke-width="1"><path d="M2 11h10l1-7-3 3-3-5-3 5-3-3z"/></svg>
  <div class="abs" style="left:44px;top:136px"><div class="label">Customer Satisfaction</div><div class="micro"><b style="color:#333;font-size:4px">103%</b> Revenue Retention<br><b style="color:#333;font-size:4px">98.2%</b> Customer would recommend</div></div>
  <div class="heading" style="left:146px;top:16px;font-size:8.5px">ABOUT BRIVANE</div>
  <svg class="abs" style="left:146px;top:32px" width="10" height="11" viewBox="0 0 10 11" fill="none" stroke="#ea0a8e" stroke-width=".8"><path d="M5 1l4 1.5v3C9 8 7 9.5 5 10.5 3 9.5 1 8 1 5.5v-3z M3.2 5.5l1.3 1.3 2.4-2.6"/></svg>
  <div class="abs" style="left:160px;top:31px;width:124px"><div style="font-size:3.6px;font-weight:700;color:var(--pink)">SECURITY</div><div class="micro">Brivane is the most secure release solution on the market. Because it is 100% native to the cloud platform, no third party servers or integrations are used and Brivane can provide any compliance attestation the platform provides.</div></div>
  <svg class="abs" style="left:146px;top:73px" width="10" height="11" viewBox="0 0 10 11" fill="none" stroke="#ea0a8e" stroke-width=".8"><path d="M5 1l4 1.5v3C9 8 7 9.5 5 10.5 3 9.5 1 8 1 5.5v-3z M3.2 5.5l1.3 1.3 2.4-2.6"/></svg>
  <div class="abs" style="left:160px;top:72px;width:62px"><div style="font-size:3.6px;font-weight:700;color:var(--pink)">TEAM STRENGTH</div><div class="micro">Our team has increased 367% in the past 3 years. We are now over 76 members strong.</div></div>
  <div class="abs" style="left:222px;top:72px;width:62px"><div style="font-size:3.6px;font-weight:700;color:var(--pink)">DIVERSITY</div><div class="micro"><b style="color:#333;font-size:4px">45%</b> Women<br><b style="color:#333;font-size:4px">43%</b> Other Minorities</div></div>
  <div class="abs micro" style="left:160px;top:93px;line-height:7px">2020 <span style="display:inline-block;width:48px;height:3.5px;background:#8f8f8f;vertical-align:middle"></span><br>2018 <span style="display:inline-block;width:16px;height:3.5px;background:#b5b5b5;vertical-align:middle"></span><br>2016 <span style="display:inline-block;width:9px;height:3.5px;background:#b5b5b5;vertical-align:middle"></span></div>
  <svg class="abs" style="left:146px;top:121px" width="10" height="11" viewBox="0 0 10 11" fill="none" stroke="#ea0a8e" stroke-width=".8"><path d="M5 1l4 1.5v3C9 8 7 9.5 5 10.5 3 9.5 1 8 1 5.5v-3z M3.2 5.5l1.3 1.3 2.4-2.6"/></svg>
  <div class="abs" style="left:160px;top:120px;width:124px"><div style="font-size:3.6px;font-weight:700;color:var(--pink)">PHILANTHROPIC WORK</div><div class="micro">The Brivane foundation sponsors more than 150 children in need. Our contributions help pay for food, education and family needs. We are also involved in water restoration projects in rural regions and aim to be a 1% equity partner.</div></div>
  <div class="foot">Presentation Title goes here | www.brivane.com</div>
  <div class="pager"><i></i><i></i><b>03</b></div>
</section>

<section class="slide" style="left:774px;top:403px;background:var(--mist)">
  <div class="heading" style="font-size:8.5px">CUSTOMERS</div>
  <p class="abs micro" style="left:15px;top:27px;width:72px">Brivane has hundreds of customers world-wide in a variety of industries.</p>
  <div class="cust-head" style="left:97px;grid-template-columns:repeat(6,30px)"><span>Government</span><span>Financial</span><span>Healthcare</span><span>Non-Profits</span><span>Consumer</span><span>Technology</span></div>
  <div class="cust-grid" style="grid-template-columns:repeat(6,25px);gap:5px 5px;left:97px;top:34px">
    <div></div><div></div><div></div><div></div><div></div><div></div>
    <div></div><div></div><div></div><div></div><div></div><div></div>
    <div></div><div></div><div></div><div></div><div></div><div></div>
    <div></div><div></div><div></div><div></div><div></div><div></div>
  </div>
  <div class="abs" style="left:0;top:110px;width:293px;height:66px;background:#fff"></div>
  <div class="abs" style="left:15px;top:122px;font-size:8.3px">Enterprise Implementation Partners</div>
  <p class="abs micro" style="left:15px;top:136px;width:80px">Brivane has more than 100 implementation firms. Referrals can be provided based on geography, industry and specialization.</p>
  <div class="abs" style="left:98px;top:142px;display:flex;gap:5px">
    <div style="width:26px;height:14px;border:.6px solid #cfd6db"></div><div style="width:26px;height:14px;border:.6px solid #cfd6db"></div><div style="width:26px;height:14px;border:.6px solid #cfd6db"></div><div style="width:26px;height:14px;border:.6px solid #cfd6db"></div><div style="width:26px;height:14px;border:.6px solid #cfd6db"></div>
  </div>
  <div class="foot">Presentation Title goes here | www.brivane.com</div>
  <div class="pager"><i></i><i></i><b>04</b></div>
</section>

<!-- Row 4 -->
<section class="slide" style="left:127px;top:606px">
  <div class="heading">THE TEAM</div>
  <div class="card-photo" role="img" aria-label="Portrait of team member in an office" style="left:15px;top:35px;background:linear-gradient(135deg,#c9dcec,#7e9fc0)"></div>
  <div class="card-info" style="left:75px;top:35px;background:var(--plum);color:#fff;border:none"><h4>Jon Marlow</h4><h5>Finance Manager</h5><p>Lorem ipsum has been the dummy text and can be replaced with your original text here regarding to this person's description</p></div>
  <div class="card-photo" role="img" aria-label="Portrait of team member" style="left:152px;top:35px;background:linear-gradient(135deg,#d8d8d8,#7a7a7a)"></div>
  <div class="card-info" style="left:210px;top:35px"><h4 style="color:var(--teal)">Gary Wendell</h4><h5>Vice President</h5><p style="color:var(--grey)">Lorem ipsum has been the dummy text and can be replaced with your original text here regarding to this person's description</p></div>
  <div class="card-photo" role="img" aria-label="Portrait of team member at a desk" style="left:15px;top:96px;background:linear-gradient(135deg,#e4edf3,#9bb8cc)"></div>
  <div class="card-info" style="left:75px;top:96px;background:var(--mist);border:none"><h4>Melina Starke</h4><h5>Marketing Manager</h5><p style="color:var(--grey)">Lorem ipsum has been the dummy text and can be replaced with your original text here regarding to this person's description</p></div>
  <div class="card-photo" role="img" aria-label="Portrait of team member" style="left:152px;top:96px;background:linear-gradient(135deg,#dedede,#8a8a8a)"></div>
  <div class="card-info" style="left:210px;top:96px"><h4 style="color:var(--teal)">Harry Gordon</h4><h5>Property Research</h5><p style="color:var(--grey)">Lorem ipsum has been the dummy text and can be replaced with your original text here regarding to this person's description</p></div>
  <div class="foot">Presentation Title goes here | www.brivane.com</div>
  <div class="pager"><i></i><i></i><b>05</b></div>
</section>

<section class="slide" style="left:450px;top:606px">
  <div class="heading">BIOGRAPHY</div>
  <div class="photo" role="img" aria-label="Portrait of executive in an office" style="left:17px;top:34px;width:76px;height:68px;background:linear-gradient(135deg,#e2ebf1,#8ea9c0)"></div>
  <div class="abs" style="left:17px;top:105px;width:76px;text-align:center"><div style="font-size:5px">Gary Wendell</div><div style="font-size:3.6px;color:var(--soft)">Vice President</div>
    <div style="display:flex;justify-content:center;gap:2px;margin:3px 0"><i style="width:5px;height:5px;border-radius:50%;background:#8d8d8d"></i><i style="width:5px;height:5px;border-radius:50%;background:#8d8d8d"></i><i style="width:5px;height:5px;border-radius:50%;background:#8d8d8d"></i></div>
    <div class="micro">P: +00 000 555 010<br>gary@northbay-advisors.com</div></div>
  <div class="abs" style="left:102px;top:34px;width:178px">
    <div class="label">Biography</div>
    <p class="micro" style="font-size:3.3px">Published author, professional speaker, coach and entrepreneur global. He is the founder and of nrstudio.com, with 23 years of unique experience in the digital services industry. His passion is to make a breakthrough in the architecture business.</p>
    <div class="label" style="margin-top:5px">Experiences</div>
    <ul class="micro" style="font-size:3.3px;padding-left:5px"><li>Managing Director at Company X, with 5 years contribution of Lorem Ipsum dolor amet nomentos nomos.</li><li>CEO at Company Trading A, as his contribution lore, ipsum dolor amet convitious mentus meritis opo ae je.</li><li>General Manager at Payment Principals ala carte del monte saos lorem ipsum dipakai terus.</li></ul>
    <div class="label" style="margin-top:5px">Certifications</div>
    <ul class="micro" style="font-size:3.3px;padding-left:5px"><li>Best Principal of The Years, Tempo Weekly 2011</li><li>Entrepreneur of Digital Business Technologies 2014</li></ul>
  </div>
  <div class="foot">Presentation Title goes here | www.brivane.com</div>
  <div class="pager"><i></i><i></i><b>06</b></div>
</section>

<section class="slide" style="left:774px;top:606px">
  <div class="heading">PROJECT SCOPE</div>
  <div class="photo" role="img" aria-label="Silhouetted colleagues by a large office window" style="left:15px;top:34px;width:274px;height:117px;background:linear-gradient(160deg,#2d2a56 0%,#7b82a8 40%,#b3bdd0 60%,#4e4670 100%)"></div>
  <div class="abs" style="left:144px;top:34px;width:127px;height:117px;background:rgba(255,255,255,.93);padding:5px 6px">
    <p class="micro" style="margin-bottom:5px">Lorem ipsum dolor sit amet, consectetur adipiscing elit, sed do eiusmod tempor incididunt ut labore et dolore magna aliqua. Ut enim ad minim veniam, quis nostrud exercitation ullamco laboris nisi commodo consequat.</p>
    <div style="display:grid;row-gap:4px">
      <div style="display:flex;gap:4px;border-bottom:.5px solid #ddd;padding-bottom:3px"><b style="font-size:4.5px;width:34px">01 LOREM IPSUM</b><span class="micro">Lorem ipsum dolor sit amet, consectetur adipiscing elit</span></div>
      <div style="display:flex;gap:4px;border-bottom:.5px solid #ddd;padding-bottom:3px"><b style="font-size:4.5px;width:34px">02 LOREM IPSUM</b><span class="micro">Lorem ipsum dolor sit amet, consectetur adipiscing elit</span></div>
      <div style="display:flex;gap:4px;border-bottom:.5px solid #ddd;padding-bottom:3px"><b style="font-size:4.5px;width:34px">03 LOREM IPSUM</b><span class="micro">Lorem ipsum dolor sit amet, consectetur adipiscing elit</span></div>
      <div style="display:flex;gap:4px"><b style="font-size:4.5px;width:34px">04 LOREM IPSUM</b><span class="micro">Lorem ipsum dolor sit amet, consectetur adipiscing elit</span></div>
    </div>
  </div>
  <div class="foot">Presentation Title goes here | www.brivane.com</div>
  <div class="pager"><i></i><i></i><b>07</b></div>
</section>

<!-- Row 5 -->
<section class="slide" style="left:127px;top:810px">
  <div class="heading">TWO COLUMN</div>
  <div class="photo" role="img" aria-label="Person walking past a tall window with city towers" style="left:15px;top:32px;width:119px;height:118px;background:linear-gradient(180deg,#8ea3b8 0%,#d6dee6 45%,#7d8894 75%,#3f3f3f 100%)"></div>
  <p class="abs" style="left:143px;top:31px;width:135px;font-size:5px;line-height:1.2;color:var(--teal)">Reprehenderit in voluptate velit esse cillum dolore eu fugiat nulla pariatur. Quis autem voluptate velit esse quam nihilista. Lorem Ipsum has been the dummy text.</p>
  <div class="num-list" style="left:143px;top:64px"><div class="num">01<p>Reprehenderit in voluptate velit esse cillum dolore eu fugiat nulla pariatur.</p></div><div class="num">02<p>Dolore eu fugiat nulla pariatur. Quis autem voluptate velit esse quam nihilista.</p></div><div class="num">05<p>Dolore eu fugiat nulla pariatur. Quis autem voluptate velit esse quam nihilista.</p></div></div>
  <div class="num-list" style="left:211px;top:64px"><div class="num">03<p>Reprehenderit in voluptate velit esse cillum dolore eu fugiat nulla pariatur.</p></div><div class="num">04<p>Dolore eu fugiat nulla pariatur. Quis autem voluptate velit esse quam nihilista.</p></div><div class="num">06<p>Dolore eu fugiat nulla pariatur. Quis autem voluptate velit esse quam nihilista.</p></div></div>
  <div class="foot">Presentation Title goes here | www.brivane.com</div>
  <div class="pager"><i></i><i></i><b>08</b></div>
</section>

<section class="slide" style="left:450px;top:810px">
  <div class="heading">TWO COLUMN</div>
  <div class="photo" role="img" aria-label="Sky above a glass office rooftop" style="left:16px;top:33px;width:120px;height:79px;background:linear-gradient(180deg,#e6edf2 0%,#c4d3de 60%,#2f4650 100%)"></div>
  <div class="photo" role="img" aria-label="Hands reviewing charts at a meeting table" style="left:151px;top:33px;width:120px;height:79px;background:linear-gradient(135deg,#3b4650,#9aa5ad 50%,#dfe3e5)"></div>
  <div class="abs" style="left:16px;top:117px;width:120px"><div class="label" style="font-size:4.8px">PROJECT NAME</div><p class="micro" style="font-size:3.4px;margin-top:1px">Lorem ipsum dolor sit amet, consectetur adipiscing elit, sed do eiusmod tempor incididunt ut labore et dolore magna aliqua.</p></div>
  <div class="abs" style="left:151px;top:117px;width:120px"><div class="label" style="font-size:4.8px">ADVISORY</div><p class="micro" style="font-size:3.4px;margin-top:1px">Ut enim ad minim veniam, quis nostrud exercitation ullamco laboris nisi ut aliquip ex ea commodo consequat.</p></div>
  <div class="foot">Presentation Title goes here | www.brivane.com</div>
  <div class="pager"><i></i><i></i><b>09</b></div>
</section>

<section class="slide" style="left:774px;top:810px">
  <div class="abs" style="left:133px;top:0;width:160px;height:176px;background:var(--mist)"></div>
  <div class="heading">PROJECT CASE</div>
  <div class="photo" role="img" aria-label="Hands typing on a laptop" style="left:0;top:36px;width:164px;height:112px;background:linear-gradient(120deg,#7c8896 0%,#c7ced5 45%,#eef0f2 70%,#a3adb6 100%)"></div>
  <div class="abs" style="left:170px;top:37px;width:90px">
    <div style="font-size:4px">Outline Brief</div><p class="micro">Lorem ipsum has been the dummy text and can be replaced with your original text here.</p>
    <div style="border-top:.5px solid #b9c5cc;margin:7px 0 3px"></div>
    <div style="font-size:4px">Methodology</div><p class="micro">Nemo enim ipsam voluptatem quia voluptas sit aspernatur aut odit aut fugit, sed quia dolores consequuntur magni.</p>
    <div style="border-top:.5px solid #b9c5cc;margin:7px 0 3px"></div>
    <div style="font-size:4px">Review</div><p class="micro">Lorem ipsum has been the dummy text and can be replaced with your original text here.</p>
  </div>
  <div class="foot">Presentation Title goes here | www.brivane.com</div>
  <div class="pager"><i></i><i></i><b>10</b></div>
</section>

<!-- Row 6 -->
<section class="slide" style="left:127px;top:1013px">
  <div class="heading">SERVICES</div>
  <div class="svc" style="left:15px;top:35px"><h6>LOREM IPSUM</h6><p>Lorem ipsum dolor sit amet, consectetur adipiscing elit, sed do eiusmod tempor incididunt ut labore et dolore magna aliqua. Lorem ipsum dolor sit amet, sed do eiusmod tempor incididunt ut labore et dolore magna aliqua consequat.</p></div>
  <div class="svc" style="left:104px;top:35px"><h6>LOREM IPSUM</h6><p>Lorem ipsum dolor sit amet, consectetur adipiscing elit, sed do eiusmod tempor incididunt ut labore et dolore magna aliqua. Lorem ipsum dolor sit amet, sed do eiusmod tempor incididunt ut labore et dolore magna aliqua consequat.</p></div>
  <div class="svc" style="left:193px;top:35px"><h6>LOREM IPSUM</h6><p>Lorem ipsum dolor sit amet, consectetur adipiscing elit, sed do eiusmod tempor incididunt ut labore et dolore magna aliqua. Lorem ipsum dolor sit amet, sed do eiusmod tempor incididunt ut labore et dolore magna aliqua consequat.</p></div>
  <div class="svc" style="left:15px;top:97px"><h6>LOREM IPSUM</h6><p>Lorem ipsum dolor sit amet, consectetur adipiscing elit, sed do eiusmod tempor incididunt ut labore et dolore magna aliqua. Lorem ipsum dolor sit amet, sed do eiusmod tempor incididunt ut labore et dolore magna aliqua consequat.</p></div>
  <div class="svc" style="left:104px;top:97px"><h6>LOREM IPSUM</h6><p>Lorem ipsum dolor sit amet, consectetur adipiscing elit, sed do eiusmod tempor incididunt ut labore et dolore magna aliqua. Lorem ipsum dolor sit amet, sed do eiusmod tempor incididunt ut labore et dolore magna aliqua consequat.</p></div>
  <div class="svc" style="left:193px;top:97px"><h6>LOREM IPSUM</h6><p>Lorem ipsum dolor sit amet, consectetur adipiscing elit, sed do eiusmod tempor incididunt ut labore et dolore magna aliqua. Lorem ipsum dolor sit amet, sed do eiusmod tempor incididunt ut labore et dolore magna aliqua consequat.</p></div>
  <div class="foot">Presentation Title goes here | www.brivane.com</div>
  <div class="pager"><i></i><i></i><b>11</b></div>
</section>

<section class="slide" style="left:450px;top:1013px">
  <div class="heading">THREE COLUMN</div>
  <div class="col3" style="left:16px"><div class="ph">IMAGE<br>PLACE HOLDER<br>0.5 X 0.5 CM<svg width="14" height="14" viewBox="0 0 14 14"><circle cx="7" cy="7" r="7" fill="#a9b8c1"/><path d="M4 7a3 3 0 1 1 3 3" stroke="#fff" stroke-width=".9" fill="none"/></svg></div><h6>LOREM IPSUM</h6><p>Lorem ipsum dolor sit amet, consectetur adipiscing elit, sed do eiusmod tempor incididunt ut labore et dolore magna aliqua.</p></div>
  <div class="col3" style="left:104px"><div class="ph">IMAGE<br>PLACE HOLDER<br>0.5 X 0.5 CM<svg width="14" height="14" viewBox="0 0 14 14"><circle cx="7" cy="7" r="7" fill="#a9b8c1"/><rect x="4" y="4" width="6" height="4.5" stroke="#fff" stroke-width=".9" fill="none"/><path d="M7 8.5v2" stroke="#fff" stroke-width=".9"/></svg></div><h6>LOREM IPSUM</h6><p>Lorem ipsum dolor sit amet, consectetur adipiscing elit, sed do eiusmod tempor incididunt ut labore et dolore magna aliqua.</p></div>
  <div class="col3" style="left:192px"><div class="ph">IMAGE<br>PLACE HOLDER<br>0.5 X 0.5 CM<svg width="14" height="14" viewBox="0 0 14 14"><circle cx="7" cy="7" r="7" fill="#a9b8c1"/><path d="M4.5 10V7 M7 10V4.5 M9.5 10V6" stroke="#fff" stroke-width="1.2"/></svg></div><h6>LOREM IPSUM</h6><p>Lorem ipsum dolor sit amet, consectetur adipiscing elit, sed do eiusmod tempor incididunt ut labore et dolore magna aliqua.</p></div>
  <div class="foot">Presentation Title goes here | www.brivane.com</div>
  <div class="pager"><i></i><i></i><b>12</b></div>
</section>

<section class="slide" style="left:774px;top:1013px">
  <div class="photo" role="img" aria-label="Busy city street between glass office towers" style="left:150px;top:0;width:143px;height:176px;background:linear-gradient(90deg,#fff 0%,rgba(255,255,255,.4) 25%,transparent 45%),linear-gradient(180deg,#e8eef2 0%,#b6c4cd 45%,#8e9aa2 75%,#6c7479 100%)"></div>
  <div class="logo" style="right:13px;top:16px;font-size:13px">Brivane</div>
  <div class="abs" style="left:34px;top:56px;font-size:10.5px;font-weight:500">THANK YOU</div>
  <svg class="abs" style="left:34px;top:74px" width="9" height="9" viewBox="0 0 9 9"><circle cx="4.5" cy="4.5" r="4.5" fill="#ea0a8e"/><path d="M2.3 3.2h4.4v2.8H2.3z M2.3 3.2l2.2 1.6 2.2-1.6" stroke="#fff" stroke-width=".5" fill="none"/></svg>
  <div class="office" style="left:49px;top:73px"><b>SAN FRANCISCO</b>210 Harbor Lane<br>Quay Tower CA 90000</div>
  <div class="office" style="left:49px;top:97px"><b>SYDNEY</b>48 Kellet Road Level 9<br>Sydney - NSW 2000</div>
  <div class="office" style="left:122px;top:73px"><b>INDIA</b>12, Lotus Park Road,<br>Andheri East,<br>Mumbai – 400000</div>
  <div class="office" style="left:122px;top:97px"><b>IRELAND</b>Unit 4, Larch House,<br>Mill Rd,<br>Dublin, Ireland</div>
  <svg class="abs" style="left:34px;top:135px" width="9" height="9" viewBox="0 0 9 9"><circle cx="4.5" cy="4.5" r="4.5" fill="#ea0a8e"/><path d="M4.5 2.2a1.6 1.6 0 0 1 1.6 1.6c0 1.2-1.6 3-1.6 3s-1.6-1.8-1.6-3a1.6 1.6 0 0 1 1.6-1.6z" fill="#fff"/></svg>
  <div class="office" style="left:49px;top:136px">hello@brivane.com<br><b>www.brivane.com</b></div>
</section>

</body>
</html>
```